Zielgruppe
Massage-Velora macht Rücken/ Ganzkörpermassage, Intim/ Körperrasur, verschiedene Wellnessanwendungen ...
Ich suche einen neutralen modernen Flyer für Hotels/ Restaurants/ Designshops wie Tolv/ Mendra ...
Leider ist mein Grafiker Anfang Mai nach Krankheit plötzlich verstorben!
Anbei viele Motive .. vielleicht finde ich hier wieder einen Partner für Anzeigen/ Aufkleber und Flyer!
Herzlichen Dank
Wilfried
Aufgabenstellung
Postkartenformat
Dopp Visitenkarte

```html
<!DOCTYPE html>
<html lang="de">
<head>
<meta charset="utf-8">
<title>Massage-Velora Flyer</title>
<link rel="stylesheet" href="https://fonts.googleapis.com/css2?family=Roboto+Condensed:wght@700&family=Roboto:wght@300;700;900&family=Arimo:wght@700&display=swap">
<style>
  :root {
    --orange: #e8820f;
    --orange-light: #f39a2c;
    --green: #93c030;
    --green-light: #b3d66a;
    --ink: #111111;
    --paper: #ffffff;
    --photo-dark: #3a2216;
    --photo-mid: #a8693f;
    --photo-light: #e2a878;
  }
  * { margin: 0; padding: 0; box-sizing: border-box; }
  html, body { width: 874px; height: 1200px; overflow: hidden; background: var(--paper); }
  .flyer { position: relative; width: 874px; height: 1200px; background: var(--paper); overflow: hidden; font-family: "Arimo", Arial, sans-serif; }
  .hero-photo { position: absolute; left: 0; top: 0; width: 874px; height: 810px; }
  .badge { position: absolute; border-radius: 50%; display: flex; flex-direction: column; align-items: center; justify-content: center; text-align: center; }
  .badge-services {
    left: -3px; top: 372px; width: 370px; height: 370px;
    background: radial-gradient(circle at 25% 30%, var(--green-light) 0%, var(--green) 45%, #86b326 100%);
    box-shadow: 0 4px 10px rgba(0,0,0,.25);
  }
  .services-list { list-style: none; transform: rotate(8deg); margin-left: 40px; margin-top: -10px; }
  .services-list li { font-weight: 700; font-size: 42px; line-height: 46px; color: var(--ink); letter-spacing: -0.5px; }
  .badge-hours {
    left: 161px; top: 194px; width: 262px; height: 262px;
    background: radial-gradient(circle at 30% 25%, var(--orange-light) 0%, var(--orange) 55%, #d9720a 100%);
    box-shadow: 0 4px 10px rgba(0,0,0,.25);
    z-index: 2;
  }
  .hours-inner { transform: rotate(-10deg); color: var(--paper); margin-top: -6px; }
  .hours-rest { font-weight: 700; font-size: 29px; line-height: 30px; }
  .hours-areas { font-weight: 700; font-size: 19px; color: var(--ink); margin: 2px 0 4px; white-space: nowrap; }
  .hours-open { font-weight: 700; font-size: 50px; line-height: 50px; }
  .brand { position: absolute; left: 0; width: 874px; text-align: center; font-family: "Roboto Condensed", "Arial Narrow", sans-serif; font-weight: 700; line-height: 1; }
  .brand-first { top: 768px; font-size: 128px; color: var(--orange); letter-spacing: 1px; }
  .brand-second { top: 866px; font-size: 128px; color: var(--green); letter-spacing: 1px; }
  .contact { position: absolute; left: 0; width: 874px; text-align: center; font-family: "Roboto", Arial, sans-serif; line-height: 1; }
  .contact-phone { top: 990px; font-weight: 300; font-size: 62px; color: var(--ink); }
  .contact-web { top: 1050px; font-weight: 900; font-size: 56px; color: var(--ink); }
  .contact-address { top: 1125px; font-weight: 700; font-size: 32px; color: var(--orange); }
</style>
</head>
<body>
<main class="flyer">
  <svg class="hero-photo" viewBox="0 0 874 810" role="img" aria-label="Foto: entspannter Mann erhält eine Rückenmassage auf einer Massageliege">
    <defs>
      <linearGradient id="photoTone" x1="0" y1="0" x2="1" y2="1">
        <stop offset="0" stop-color="var(--photo-dark)"/>
        <stop offset="0.35" stop-color="var(--photo-mid)"/>
        <stop offset="0.65" stop-color="var(--photo-light)"/>
        <stop offset="1" stop-color="var(--photo-mid)"/>
      </linearGradient>
    </defs>
    <polygon points="0,0 874,0 874,804 0,619" fill="url(#photoTone)"/>
  </svg>

  <div class="badge badge-hours">
    <div class="hours-inner">
      <p class="hours-rest">Kein<br>Ruhetag</p>
      <p class="hours-areas">Haus / Hotel / Outcall</p>
      <p class="hours-open">OPEN<br>DAILY</p>
    </div>
  </div>

  <div class="badge badge-services">
    <ul class="services-list">
      <li>Ganzkörper</li>
      <li>Pro Relax</li>
      <li>Intimrasur</li>
      <li>Streicheln</li>
      <li>Tantra</li>
    </ul>
  </div>

  <h1 class="brand brand-first">MASSAGE</h1>
  <p class="brand brand-second">VELORA</p>

  <p class="contact contact-phone">Tel. 0175 - 482 19 63</p>
  <p class="contact contact-web">massage-velora.com</p>
  <p class="contact contact-address">City Studio, Falkgasse 12/ 4.OG, 80331 München</p>
</main>
</body>
</html>
```